eBook Cover_H. Vollmar-Tessen
Schnell und zuverlässoig,Änderungswünsche wurden umgehend ausgeführt. Vielen Dank für das tolle Cover zu meinem ersten Buch!
Zielgruppe
freie Roman-Autorin (Erstlingswerk)
Zielgruppe: Lesende (Erwachsene), Frauen
Charakterisierung: magisch-realistischer Familienroman, spielt im Europa der Jetzt-Zeit
Aufgabenstellung
Im ersten Schritt geht es um ein Cover für ein eBook, das aber bei Bedarf als Book on Demand gedruckt werden soll. Es wird daher später Anforderung bzgl. Dicke / Umfang des gedruckten Buches und einer Rückseite geben. Das gewählte Design soll dann dahingehend überarbeitet und finale Druckdaten zur Verfügung gestellt werden. Dies soll von vornherein berücksichtigt werden und im Preis enthalten sein.
Titel: Nebel über Glas, Funken im Moor
Autorinnenname: Henrike Vollmar-Tessen
des weiteren auf dem Cover: Roman

```html
<!DOCTYPE html>
<html lang="de">
<head>
<meta charset="utf-8">
<title>Nebel über Glas, Funken im Moor – Cover</title>
<link rel="stylesheet" href="https://fonts.googleapis.com/css2?family=Oswald:wght@700&family=Open+Sans:wght@600&display=swap">
<style>
  :root {
    --backdrop: #eceeef;
    --paper: #ffffff;
    --green-light: #5cf05a;
    --green-mid: #33d333;
    --green-deep: #1aa81c;
    --ink: #555d66;
    --roman-white: #ffffff;
  }
  * { margin: 0; padding: 0; box-sizing: border-box; }
  html, body {
    width: 948px;
    height: 1200px;
    overflow: hidden;
    background: var(--backdrop);
  }
  .cover {
    position: absolute;
    left: 74px;
    top: 45px;
    width: 800px;
    height: 1110px;
    background: var(--paper);
    overflow: hidden;
  }
  .cover__art {
    position: absolute;
    inset: 0;
    width: 800px;
    height: 1110px;
  }
  .cover__author {
    position: absolute;
    left: 400px;
    top: 330px;
    width: 300px;
    text-align: center;
    font-family: "Open Sans", Arial, sans-serif;
    font-weight: 600;
    font-size: 21px;
    letter-spacing: 0.5px;
    color: var(--ink);
  }
  .cover__rule {
    position: absolute;
    left: 450px;
    top: 368px;
    width: 200px;
    height: 4px;
    background: var(--ink);
  }
  .cover__title {
    position: absolute;
    left: 336px;
    top: 400px;
    font-family: "Oswald", "Arial Narrow", sans-serif;
    font-weight: 700;
    font-size: 56px;
    line-height: 68px;
    letter-spacing: 1.5px;
    color: var(--ink);
    text-transform: uppercase;
    white-space: nowrap;
  }
  .cover__genre {
    position: absolute;
    left: 96px;
    top: 1000px;
    font-family: "Oswald", "Arial Narrow", sans-serif;
    font-weight: 700;
    font-size: 44px;
    letter-spacing: 2px;
    color: var(--roman-white);
  }
</style>
</head>
<body>
  <main class="cover">
    <svg class="cover__art" viewBox="0 0 800 1110" role="img" aria-label="Grüne Fläche mit hellen, wellenförmig geschwungenen Linien und Kreismuster">
      <defs>
        <linearGradient id="greenField" x1="0" y1="0" x2="1" y2="1">
          <stop offset="0" stop-color="var(--green-mid)"/>
          <stop offset="0.45" stop-color="var(--green-light)"/>
          <stop offset="1" stop-color="var(--green-deep)"/>
        </linearGradient>
      </defs>
      <polygon points="0,0 448,0 304,533 376,1110 0,1110" fill="url(#greenField)"/>
    </svg>

    <p class="cover__author">HENRIKE VOLLMAR-TESSEN</p>
    <div class="cover__rule"></div>
    <h1 class="cover__title">Nebel über Glas<br>Funken im Moor</h1>
    <p class="cover__genre">ROMAN</p>
  </main>
</body>
</html>
```